Creative designs Needed! Dieting Tips for Nurses

Need a creative design for my first book that is targeted to nurses that want to lose weight.
THE TITLE OF MY BOOK IS:
The Bright Lantern Pantry Uprising:
9 Slim-Down Tricks Each Caregiver Should Learn!

- My audience is female.

- My colors for my business are red, black, gray and white however feel free to use other colors

- The cover should note there is Free Bonus Content.

- The book cover should have a fun modern feel to it.

- Since the title is talking about time. I think there should be some sort of clock in the design. Not an actual clock but a clock design.

- Please let me know if you need anything from me to complete your design. I go by Coach Brin.

- Subject of book is dieting tips for nurses

Target Market(s)

Nurses

Industry/Entity Type

Health And Wellness

Font styles to use
Serif

Colors
ec1f27
1b1b1b
dddddd

Requirements
Must have
• List the Free Bonus Content label on the front cover
• Must keep in mind there will be sequels to this book for other target markets
• • Should be creative, modern
• • Please try not to use stock images with just the text for this design - I am looking for something creative and unique.
• • Something that plays with the idea of time, think clock.
• • Need something out the box!!
• • Think diversity in the people if you do opt to use images - Would prefer if you steer clear of regular photos of people
• • If you do use an image of a nurse, please note nurses mostly wear scrubs today - so think about that in your concepts
Nice to have
• The design should be clever
Should not have
• Although I selected the 3 colors feel free to explore other colors and those 3 colors do not have to be the dominate colors.
• The book design should pop out to people when they see it.

```html
<!DOCTYPE html>
<html lang="en">
<head>
<meta charset="utf-8">
<title>The Bright Lantern Pantry Uprising — Coach Brin</title>
<link rel="stylesheet" href="https://fonts.googleapis.com/css2?family=Playfair+Display:ital,wght@1,700;1,900&family=Bodoni+Moda:wght@700;800&display=swap">
<style>
  :root {
    --paper: #ffffff;
    --green: #6cc474;
    --ink: #111111;
    --plate: #f6f5f1;
    --plate-edge: #e3e6ef;
    --tomato: #f08a66;
    --basil: #6f9a58;
    --steel: #b9bec4;
    --steel-dark: #8d939a;
  }
  html, body {
    margin: 0;
    padding: 0;
    overflow: hidden;
    background: var(--paper);
  }
  .cover {
    position: relative;
    width: 750px;
    height: 1200px;
    background: var(--paper);
    overflow: hidden;
  }
  .title {
    position: absolute;
    left: 22px;
    top: 14px;
    margin: 0;
    font-family: "Playfair Display", serif;
    font-style: italic;
    font-weight: 900;
    font-size: 78px;
    line-height: 104px;
    letter-spacing: -1px;
    color: var(--green);
    z-index: 3;
  }
  .title .accent { color: var(--ink); }
  .subtitle {
    position: absolute;
    left: 28px;
    top: 284px;
    margin: 0;
    font-family: "Bodoni Moda", serif;
    font-weight: 800;
    font-size: 40px;
    line-height: 66px;
    color: var(--ink);
    z-index: 3;
  }
  .bonus {
    position: absolute;
    left: 28px;
    top: 572px;
    margin: 0;
    padding: 8px 16px;
    border: 2px solid var(--ink);
    border-radius: 22px;
    font-family: "Bodoni Moda", serif;
    font-weight: 800;
    font-size: 18px;
    letter-spacing: 2px;
    color: var(--ink);
    background: var(--paper);
    z-index: 3;
  }
  .dish-photo {
    position: absolute;
    left: 0;
    top: 0;
    width: 750px;
    height: 1200px;
    z-index: 1;
  }
  .clock-face {
    position: absolute;
    left: 0;
    top: 0;
    width: 750px;
    height: 1200px;
    z-index: 2;
  }
  .dot {
    position: absolute;
    border-radius: 50%;
    background: var(--green);
    z-index: 2;
  }
  .dot--left { left: 88px; top: 772px; width: 32px; height: 32px; }
  .dot--bottom { left: 438px; top: 1142px; width: 32px; height: 32px; }
  .author {
    position: absolute;
    left: 16px;
    top: 1026px;
    margin: 0;
    font-family: "Bodoni Moda", serif;
    font-weight: 800;
    font-size: 90px;
    line-height: 1;
    color: var(--green);
    z-index: 3;
  }
  .author .accent { color: var(--ink); }
</style>
</head>
<body>
  <main class="cover">
    <svg class="dish-photo" viewBox="0 0 750 1200" role="img" aria-label="Photo of a gloved hand setting a knife and fork as clock hands on a plate of tomato, mozzarella and basil salad">
      <defs>
        <radialGradient id="dish-tones" cx="50%" cy="50%" r="50%">
          <stop offset="0" stop-color="var(--basil)" stop-opacity="0.55"/>
          <stop offset="0.45" stop-color="var(--tomato)" stop-opacity="0.55"/>
          <stop offset="0.78" stop-color="var(--plate)"/>
          <stop offset="1" stop-color="var(--plate-edge)"/>
        </radialGradient>
      </defs>
      <circle cx="460" cy="772" r="298" fill="url(#dish-tones)"/>
    </svg>

    <svg class="clock-face" viewBox="0 0 750 1200" aria-hidden="true">
      <g stroke="var(--steel-dark)" stroke-width="4" stroke-linecap="round">
        <line x1="460" y1="492" x2="460" y2="512"/>
        <line x1="740" y1="772" x2="720" y2="772"/>
        <line x1="460" y1="1052" x2="460" y2="1032"/>
        <line x1="180" y1="772" x2="200" y2="772"/>
      </g>
      <line class="hand-hour" x1="460" y1="728" x2="460" y2="226" stroke="var(--steel)" stroke-width="16" stroke-linecap="round"/>
      <line class="hand-minute" x1="462" y1="748" x2="738" y2="1130" stroke="var(--steel)" stroke-width="10" stroke-linecap="round"/>
      <circle cx="460" cy="740" r="9" fill="var(--steel-dark)"/>
    </svg>

    <h1 class="title">The <span class="accent">Bright</span> Lantern<br>Pantry Uprising:</h1>

    <p class="subtitle">9 Slim-Down<br>Tricks Each<br>Caregiver<br>Should Learn!</p>

    <p class="bonus">FREE BONUS CONTENT</p>

    <span class="dot dot--left"></span>
    <span class="dot dot--bottom"></span>

    <p class="author">Coach <span class="accent">Brin</span></p>
  </main>
</body>
</html>
```